Meridane Works, Inc. - Update our Website

Meridane Works needs a website to help our customers to navigate through our services efficiently. Our existing website is at www.tovrel.net

We would like to explain our services with content and pictures (photographs) that distinguishes our products and services from our competition.

The website design must implement a strategy to focus on our Contract Labeling services.

With this new design we would like to attract new customers and ensure that our existing customers are fully informed with our latest offerings.

```html
<!DOCTYPE html>
<html lang="en">
<head>
<meta charset="utf-8">
<title>Meridane Works, Inc.</title>
<link href="https://fonts.googleapis.com/css2?family=Montserrat:wght@700&family=Open+Sans:wght@400;600&family=Raleway:wght@600;700;800&display=swap" rel="stylesheet">
<style>
:root{
  --ink:#111;
  --muted:#8a8a8a;
  --white:#fff;
  --grey-band:#f1f1f1;
  --tag-blue:#1414e6;
  --placeholder:#2a2a2a;
  --footer:#333;
  --footer-bottom:#222;
  --footer-text:#9a9a9a;
  --accent-line:#4a8fc9;
}
*{margin:0;padding:0;box-sizing:border-box}
html,body{width:1200px;height:2656px;overflow:hidden;background:var(--white)}
body{position:relative;font-family:'Open Sans',sans-serif;color:var(--ink)}

/* header */
.site-header{position:absolute;left:0;top:0;width:1200px;height:105px;background:var(--white)}
.brand{position:absolute;left:80px;top:38px;display:flex;align-items:center;gap:10px;font-family:'Raleway',sans-serif;font-weight:800;font-size:17px;letter-spacing:.5px;color:var(--ink);text-transform:uppercase}
.brand-dot{width:24px;height:24px;border-radius:50%;background:#1d8e3e}
.main-nav{position:absolute;top:47px;left:595px;display:flex;font-family:'Raleway',sans-serif;font-weight:700;font-size:10.5px;letter-spacing:1.4px}
.main-nav span{display:inline-block;margin-right:44px}
.main-nav span.drop::after{content:"";display:inline-block;width:4px;height:4px;border-right:1.5px solid var(--ink);border-bottom:1.5px solid var(--ink);transform:rotate(45deg);margin-left:6px;vertical-align:3px}

/* hero */
.hero{position:absolute;left:0;top:105px;width:1200px;height:561px;background:radial-gradient(ellipse at 62% 40%,#e7ecf2 0%,#9fb7d4 28%,#2f6fb4 58%,#0a3f8a 100%)}
.hero-title{position:absolute;top:160px;width:100%;text-align:center;font-family:'Montserrat',sans-serif;font-weight:700;font-size:51px;letter-spacing:1px;color:var(--white)}
.hero-title span{border-bottom:3px solid var(--white);padding-bottom:2px}
.hero-sub{position:absolute;top:255px;width:100%;text-align:center;font-size:17.5px;color:var(--white)}
.btn{position:absolute;top:340px;height:50px;display:flex;align-items:center;justify-content:center;font-family:'Raleway',sans-serif;font-weight:700;font-size:11px;letter-spacing:1.2px;border-radius:3px}
.btn-ghost{left:480px;width:100px;border:2px solid var(--white);color:var(--white)}
.btn-solid{left:605px;width:115px;background:var(--white);color:var(--ink)}
.hero-arrow{position:absolute;top:261px}
.hero-dots{position:absolute;top:498px;left:579px;display:flex;gap:10px}
.hero-dots i{width:7px;height:7px;border-radius:50%;background:rgba(255,255,255,.5)}
.hero-dots i.on{background:var(--white)}

/* services */
.services{position:absolute;left:0;top:666px;width:1200px;height:391px}
.service{position:absolute;top:80px;width:320px;text-align:center}
.service-visual{width:72px;height:84px;margin:0 auto;border-radius:6px;background:var(--placeholder)}
.service h3{margin-top:30px;font-family:'Raleway',sans-serif;font-weight:800;font-size:13px;letter-spacing:1.5px}
.service p{margin-top:40px;font-size:12.5px;line-height:20px;color:var(--muted)}

/* features */
.features{position:absolute;left:0;top:1057px;width:1200px;height:447px;background:var(--grey-band)}
.features-title{position:absolute;top:80px;width:100%;text-align:center;font-family:'Raleway',sans-serif;font-weight:800;font-size:13.5px;letter-spacing:1.6px}
.features-title span{border-bottom:2px solid var(--ink);padding-bottom:8px}
.feature{position:absolute;width:300px}
.feature svg{position:absolute;left:0;top:0}
.feature h4{position:absolute;left:66px;top:0;font-family:'Raleway',sans-serif;font-weight:800;font-size:13px;letter-spacing:1.4px;white-space:nowrap}
.feature .rule{position:absolute;left:66px;top:30px;width:34px;height:2px;background:var(--ink)}
.feature p{position:absolute;left:66px;top:52px;width:245px;font-size:12.5px;line-height:20px;color:var(--muted)}

/* products */
.products{position:absolute;left:0;top:1504px;width:1200px;height:490px;background:linear-gradient(160deg,#c9d6e6 0%,#7d95d0 40%,#3d52c4 75%,#5a6fcf 100%)}
.product{position:absolute;top:191px;width:133px;text-align:center}
.product-box{width:133px;height:133px;border:2px solid var(--white);display:flex;align-items:center;justify-content:center}
.product-stem{width:2px;height:23px;background:var(--white);margin:0 auto}
.product-label{margin-top:14px;font-family:'Raleway',sans-serif;font-weight:800;font-size:13px;letter-spacing:1.6px;color:var(--white)}

/* tagline */
.tagline{position:absolute;top:2052px;width:100%;text-align:center;font-family:'Raleway',sans-serif;font-weight:600;font-size:22px;letter-spacing:2.5px;color:#333}
.tagline span{border-bottom:2px solid var(--accent-line);padding-bottom:6px}

/* footer */
.site-footer{position:absolute;left:0;top:2145px;width:1200px;height:392px;background:var(--footer);color:var(--footer-text);font-size:11.5px;line-height:18px}
.footer-brand{position:absolute;left:80px;top:86px;display:flex;align-items:center;gap:10px;font-family:'Raleway',sans-serif;font-weight:800;font-size:17px;letter-spacing:.5px;color:var(--white);text-transform:uppercase}
.footer-about{position:absolute;left:80px;top:157px;width:260px}
.footer-heading{position:absolute;left:612px;top:81px;font-family:'Raleway',sans-serif;font-weight:700;font-size:10px;letter-spacing:1.8px;color:var(--white)}
.office{position:absolute;left:612px;font-size:11px;text-transform:uppercase}
.contact{position:absolute;left:881px;font-size:11.5px}
.contact div{display:flex;align-items:center;gap:8px}
.footer-bottom{position:absolute;left:0;top:2537px;width:1200px;height:119px;background:var(--footer-bottom)}
.copyright{position:absolute;left:80px;top:46px;font-size:10px;color:var(--footer-text)}
.social{position:absolute;left:925px;top:45px;display:flex;gap:31px}
.social i{width:12px;height:12px;border-radius:50%;background:var(--white)}
</style>
</head>
<body>

<header class="site-header">
  <div class="brand"><span class="brand-dot"></span>Meridane Works, Inc.</div>
  <nav class="main-nav">
    <span class="drop">HOME</span><span class="drop">PAGES</span><span class="drop">WORK</span><span class="drop">BLOG</span><span>ELEMENTS</span><span class="drop">CONTACT</span>
  </nav>
</header>

<section class="hero" role="img" aria-label="Photograph of a gloved hand holding a round laboratory flask that contains a small globe">
  <h1 class="hero-title"><span>MERIDANE WORKS, INC.</span></h1>
  <p class="hero-sub">Specializes in providing products and services to the pharmaceutical industry.</p>
  <div class="btn btn-ghost">ABOUT US</div>
  <div class="btn btn-solid">CONTACT US</div>
  <svg class="hero-arrow" style="left:14px" width="56" height="56" viewBox="0 0 56 56"><circle cx="28" cy="28" r="26" fill="none" stroke="#fff" stroke-width="2"/><path d="M38 28H18M25 21l-7 7 7 7" fill="none" stroke="#fff" stroke-width="2"/></svg>
  <svg class="hero-arrow" style="left:1130px" width="56" height="56" viewBox="0 0 56 56"><circle cx="28" cy="28" r="26" fill="none" stroke="#fff" stroke-width="2"/><path d="M18 28h20M31 21l7 7-7 7" fill="none" stroke="#fff" stroke-width="2"/></svg>
  <div class="hero-dots"><i></i><i></i><i class="on"></i></div>
</section>

<section class="services">
  <div class="service" style="left:84px">
    <div class="service-visual" role="img" aria-label="Illustration of a labelled medicine bottle with a capsule"></div>
    <h3>MERISERV</h3>
    <p>MeriBook labels include multiple pages of study information within each clinical label to address the needs of multi-language studies.</p>
  </div>
  <div class="service" style="left:440px">
    <div class="service-visual" role="img" aria-label="Illustration of a labelled medicine bottle inside a globe stand"></div>
    <h3>MERIBOOK-CLINICAL BOOKLET LABELS</h3>
    <p>MeriBook labels include multiple pages of study information within each clinical label to address the needs of multi-language studies.</p>
  </div>
  <div class="service" style="left:796px">
    <div class="service-visual" role="img" aria-label="Illustration of a labelled medicine bottle beside a die"></div>
    <h3>CLINICAL RANDOMIZATION</h3>
    <p>MeriBook labels include multiple pages of study information within each clinical label to address the needs of multi-language studies.</p>
  </div>
</section>

<section class="features">
  <h2 class="features-title"><span>MERIPRO/LBL CLINICAL LABEL GENERATION SYSTEM</span></h2>
  <div class="feature" style="left:80px;top:145px">
    <svg width="44" height="44" viewBox="0 0 44 44"><path d="M2 2h20l20 20-18 20L2 22z" fill="var(--tag-blue)"/><circle cx="10" cy="10" r="3" fill="#f1f1f1"/></svg>
    <h4>COMPREHENSIVE SYSTEM DESIGN</h4><div class="rule"></div>
    <p>At vero eos et accusamus et iusto odio dignissimos ducimus qui praesentium voluptatum</p>
  </div>
  <div class="feature" style="left:436px;top:145px">
    <svg width="44" height="44" viewBox="0 0 44 44"><path d="M2 2h20l20 20-18 20L2 22z" fill="var(--tag-blue)"/><circle cx="10" cy="10" r="3" fill="#f1f1f1"/></svg>
    <h4>COMPLIANCE</h4><div class="rule"></div>
    <p>At vero eos et accusamus et iusto odio dignissimos ducimus qui praesentium voluptatum</p>
  </div>
  <div class="feature" style="left:792px;top:145px">
    <svg width="44" height="44" viewBox="0 0 44 44"><path d="M2 2h20l20 20-18 20L2 22z" fill="var(--tag-blue)"/><circle cx="10" cy="10" r="3" fill="#f1f1f1"/></svg>
    <h4>STATISTICS</h4><div class="rule"></div>
    <p>At vero eos et accusamus et iusto odio dignissimos ducimus qui praesentium voluptatum</p>
  </div>
  <div class="feature" style="left:80px;top:297px">
    <svg width="44" height="44" viewBox="0 0 44 44"><path d="M2 2h20l20 20-18 20L2 22z" fill="var(--tag-blue)"/><circle cx="10" cy="10" r="3" fill="#f1f1f1"/></svg>
    <h4>LABEL DESIGN</h4><div class="rule"></div>
    <p>At vero eos et accusamus et iusto odio dignissimos ducimus qui praesentium voluptatum</p>
  </div>
  <div class="feature" style="left:436px;top:297px">
    <svg width="44" height="44" viewBox="0 0 44 44"><path d="M2 2h20l20 20-18 20L2 22z" fill="var(--tag-blue)"/><circle cx="10" cy="10" r="3" fill="#f1f1f1"/></svg>
    <h4>GLOBAL SOLUTION</h4><div class="rule"></div>
    <p>At vero eos et accusamus et iusto odio dignissimos ducimus qui praesentium voluptatum</p>
  </div>
  <div class="feature" style="left:792px;top:297px">
    <svg width="44" height="44" viewBox="0 0 44 44"><path d="M2 2h20l20 20-18 20L2 22z" fill="var(--tag-blue)"/><circle cx="10" cy="10" r="3" fill="#f1f1f1"/></svg>
    <h4>SECURITY FEATURES</h4><div class="rule"></div>
    <p>At vero eos et accusamus et iusto odio dignissimos ducimus qui praesentium voluptatum</p>
  </div>
</section>

<section class="products" role="img" aria-label="Photograph of rows of glass test tubes with a pipette dropping green liquid">
  <div class="product" style="left:134px">
    <div class="product-box"><svg width="34" height="40" viewBox="0 0 34 40" fill="none" stroke="#fff" stroke-width="1.5"><rect x="6" y="2" width="24" height="36"/><path d="M2 8h6M2 14h6M2 20h6M2 26h6M2 32h6M13 10h12"/></svg></div>
    <div class="product-stem"></div><div class="product-label">MERIBOOK◆</div>
  </div>
  <div class="product" style="left:400px">
    <div class="product-box"><svg width="40" height="40" viewBox="0 0 40 40" fill="none" stroke="#fff" stroke-width="1.5"><circle cx="20" cy="8" r="4"/><path d="M18 12 8 36M22 12l10 24M6 26c8 5 20 5 28 0"/></svg></div>
    <div class="product-stem"></div><div class="product-label">MERISERV◆</div>
  </div>
  <div class="product" style="left:668px">
    <div class="product-box"><svg width="42" height="42" viewBox="0 0 42 42" fill="none" stroke="#fff" stroke-width="1.5"><ellipse cx="21" cy="21" rx="19" ry="7"/><ellipse cx="21" cy="21" rx="19" ry="7" transform="rotate(60 21 21)"/><ellipse cx="21" cy="21" rx="19" ry="7" transform="rotate(-60 21 21)"/><circle cx="21" cy="21" r="2.5" fill="#fff"/></svg></div>
    <div class="product-stem"></div><div class="product-label">MERIPRO/LBL◆</div>
  </div>
  <div class="product" style="left:935px">
    <div class="product-box"><svg width="42" height="42" viewBox="0 0 42 42" fill="none" stroke="#fff" stroke-width="1.5"><path d="M21 4 39 13 21 22 3 13z"/><path d="M3 21l18 9 18-9M3 29l18 9 18-9"/></svg></div>
    <div class="product-stem"></div><div class="product-label">MERISTOCK◆</div>
  </div>
</section>

<h2 class="tagline"><span>MERIDANE WORKS, INC.</span></h2>

<footer class="site-footer">
  <div class="footer-brand"><span class="brand-dot"></span>Meridane Works, Inc.</div>
  <p class="footer-about">Meridane Works, Inc. specializes in providing products and services to the pharmaceutical industry.</p>
  <h3 class="footer-heading">OFFICE LOCATIONS</h3>
  <p class="office" style="top:157px">412 Linden Street<br>Harbor Vale<br>NY 10990-2210 USA</p>
  <p class="office" style="top:230px">88 Alder Row<br>Brookmere<br>NJ 07990 USA</p>
  <div class="contact" style="top:157px">
    <div><svg width="11" height="11" viewBox="0 0 12 12"><path d="M2 1l3 0 1 3-2 1c1 2 2 3 3 3l1-2 3 1v3c-6 0-9-4-9-9z" fill="#ddd"/></svg>+1-555-014-6200</div>
    <div><svg width="11" height="9" viewBox="0 0 12 9"><rect width="12" height="9" fill="#ddd"/><path d="M0 0l6 5 6-5" fill="none" stroke="#333"/></svg>office.ny@meridaneworks.net</div>
  </div>
  <div class="contact" style="top:230px">
    <div><svg width="11" height="11" viewBox="0 0 12 12"><path d="M2 1l3 0 1 3-2 1c1 2 2 3 3 3l1-2 3 1v3c-6 0-9-4-9-9z" fill="#ddd"/></svg>+1-555-017-0040</div>
    <div><svg width="11" height="9" viewBox="0 0 12 9"><rect width="12" height="9" fill="#ddd"/><path d="M0 0l6 5 6-5" fill="none" stroke="#333"/></svg>office.nj@meridaneworks.net</div>
  </div>
</footer>
<div class="footer-bottom">
  <p class="copyright">© 2014 Meridane Works - All Rights Reserved</p>
  <div class="social"><i></i><i></i><i></i><i></i><i></i></div>
</div>

</body>
</html>
```